young adult fiction novel titled 'Chronicles of the Lanterns - The Heron's Vigil'

Introduction
Hello! Attached you will find a combination of my own amateurish attempts at graphic design and also pictures that have inspired me. With the obvious exception of the ‘Crown of Embers’ and ‘Keeper of the Wells’ stuff, I have purchased the other images so they are fair game to be used (contact me if you want the hi-res versions).
I hope that by showing you these, I might be able to convey what I’m looking for in a front cover and a website. I’d just like to make a few points that might also help you understand a little better.
1. The book is called ‘The Heron’s Vigil’. It is a 'knights of the round table' type story so I would like
2. My concept is 12 tales, each told by a member of the zodiac. I would like the first front cover to be designed in such a way that the following 11 can be thematically linked together. The Heron’s Vigil is obviously the Capricorn’s tale.
3. As Capricorn is an earth sign, I would like the colour scheme to be green and brown. I would also definitely like the motto to be ‘Bend the River Back’.
4. The name of the series will be ‘Chronicles of the Lanterns’ and I would like this written somewhere on the front cover.
5. My Nom de Plume is going to be RM Calloway.
6. There is room for quirkiness in the design. The book itself is, I may say so, dryly humourous and, also, is set in the future. This allows for a slight twist on more traditional heraldry.
7. It would be nice to include a stylised zodiac wheel that could appear on all the books and the website. It would be one of the motifs that links the books together. In the story, a round table of the zodiac is set up. This is a fusion of astrology and Arthurian legend.
8. My main concern with my own design is the colouring. I was concerned that it looked a little cheap to have a single matt colour. I was thinking that some sort of texture of w/e might add a bit of quality to the design. This is not a deal breaker and, as I said, I would regard it as a safe option if the above change is made.
9. My perfect design would be more like an ACTUAL shield with elements of classic heraldry but a a subtle nod to dystopian rust saint / ashen trials type art work.
Updates
Reason: I have one very strong contender but several other strong drafts on the table and want to give them a chance to improve their designs.
Target Market(s)
Western Teenagers who read fantasy novels such as KOTW, crown of embers, Milo Brackwind etc
Industry/Entity Type
Graphic Design

```html
<!DOCTYPE html>
<html lang="en">
<head>
<meta charset="UTF-8">
<title>Chronicles of the Lanterns – The Heron's Vigil – Front Cover</title>
<link rel="stylesheet" href="https://fonts.googleapis.com/css2?family=Josefin+Sans:wght@300;400&family=EB+Garamond:wght@400&family=Noto+Sans+Symbols:wght@400;700&family=Noto+Sans+Symbols+2&display=swap">
<style>
  :root {
    --page-bg: #ffffff;
    --cover-green-light: #55722f;
    --cover-green-mid: #44662a;
    --cover-green-deep: #2f5a22;
    --ink-white: #f4f1e6;
    --ink-black: #0d0d0b;
    --ornament-tone: rgba(244, 241, 230, 0.55);
    --emblem-tone: #1a2412;
  }
  * { box-sizing: border-box; margin: 0; padding: 0; }
  html, body {
    width: 1200px;
    height: 851px;
    overflow: hidden;
    background: var(--page-bg);
  }
  .canvas {
    position: relative;
    width: 1200px;
    height: 851px;
  }
  .cover {
    position: absolute;
    left: 362px;
    top: 110px;
    width: 470px;
    height: 650px;
    background:
      radial-gradient(ellipse at 30% 20%, rgba(255,255,255,0.06), transparent 60%),
      radial-gradient(ellipse at 75% 70%, rgba(0,0,0,0.10), transparent 55%),
      linear-gradient(180deg, var(--cover-green-light) 0%, var(--cover-green-mid) 45%, var(--cover-green-deep) 100%);
    color: var(--ink-white);
  }
  .corner-ornament {
    position: absolute;
    background: var(--ornament-tone);
    opacity: 0.5;
    border-radius: 4px;
  }
  .corner-ornament--top-left { left: 12px; top: 24px; width: 52px; height: 48px; }
  .corner-ornament--top-right { right: 12px; top: 24px; width: 52px; height: 48px; }
  .corner-ornament--bottom-left { left: 12px; bottom: 8px; width: 26px; height: 18px; }
  .corner-ornament--bottom-right { right: 12px; bottom: 8px; width: 26px; height: 18px; }
  .series-initial {
    position: absolute;
    left: 50%;
    top: 42px;
    width: 60px;
    height: 104px;
    transform: translateX(-50%);
    background: var(--ornament-tone);
    opacity: 0.6;
    border-radius: 30px 30px 26px 26px;
  }
  .series-title {
    position: absolute;
    left: 0;
    right: 0;
    top: 172px;
    text-align: center;
    white-space: nowrap;
    font-family: 'Josefin Sans', sans-serif;
    font-weight: 300;
    font-size: 28px;
    letter-spacing: 0.3px;
    text-transform: uppercase;
    line-height: 1;
  }
  .book-title {
    position: absolute;
    left: 0;
    right: 0;
    top: 218px;
    display: flex;
    justify-content: center;
    align-items: center;
    gap: 12px;
    white-space: nowrap;
    font-family: 'Josefin Sans', sans-serif;
    font-weight: 300;
    font-size: 19px;
    letter-spacing: 0.5px;
    text-transform: uppercase;
    line-height: 1;
  }
  .title-flourish {
    display: inline-block;
    width: 16px;
    height: 8px;
    background: var(--ornament-tone);
    border-radius: 4px;
  }
  .zodiac-wheel {
    position: absolute;
    left: 35px;
    top: 245px;
    width: 400px;
    height: 400px;
  }
  .zodiac-wheel .sign {
    font-family: 'Noto Sans Symbols', 'Noto Sans Symbols 2', sans-serif;
    font-size: 28px;
    font-weight: 700;
    fill: var(--ink-black);
  }
  .zodiac-wheel .sign--current { fill: var(--ink-white); }
  .zodiac-wheel .ring {
    fill: none;
    stroke: var(--ink-black);
    stroke-width: 12;
  }
  .author {
    position: absolute;
    left: 0;
    right: 0;
    bottom: 10px;
    text-align: center;
    font-family: 'EB Garamond', serif;
    font-size: 16px;
    line-height: 1;
    color: var(--ink-white);
  }
</style>
</head>
<body>
<main class="canvas">
  <section class="cover">
    <div class="corner-ornament corner-ornament--top-left" role="img" aria-label="Scrolling corner flourish"></div>
    <div class="corner-ornament corner-ornament--top-right" role="img" aria-label="Scrolling corner flourish"></div>

    <div class="series-initial" role="img" aria-label="Ornate illuminated initial letter, series emblem"></div>

    <h1 class="series-title">Chronicles of the Lanterns</h1>
    <p class="book-title">
      <span class="title-flourish" role="img" aria-label="Small flourish"></span>
      The Heron’s Vigil
      <span class="title-flourish" role="img" aria-label="Small flourish"></span>
    </p>

    <svg class="zodiac-wheel" viewBox="0 0 400 400" aria-label="Zodiac wheel">
      <defs>
        <radialGradient id="emblem-fill" cx="50%" cy="50%" r="50%">
          <stop offset="0%" stop-color="#1a2412" stop-opacity="0.85"/>
          <stop offset="100%" stop-color="#1a2412" stop-opacity="0.35"/>
        </radialGradient>
      </defs>
      <g text-anchor="middle" dominant-baseline="central">
        <text class="sign" x="200" y="50">♏&#xFE0E;</text>
        <text class="sign" x="275" y="70.1">♎&#xFE0E;</text>
        <text class="sign" x="329.9" y="125">♍&#xFE0E;</text>
        <text class="sign" x="350" y="200">♌&#xFE0E;</text>
        <text class="sign" x="329.9" y="275">♋&#xFE0E;</text>
        <text class="sign" x="275" y="329.9">♊&#xFE0E;</text>
        <text class="sign" x="200" y="350">♉&#xFE0E;</text>
        <text class="sign" x="125" y="329.9">♈&#xFE0E;</text>
        <text class="sign" x="70.1" y="275">♓&#xFE0E;</text>
        <text class="sign" x="50" y="200">♒&#xFE0E;</text>
        <text class="sign sign--current" x="70.1" y="125">♑&#xFE0E;</text>
        <text class="sign" x="125" y="70.1">♐&#xFE0E;</text>
      </g>
      <circle class="ring" cx="200" cy="200" r="112"/>
      <g role="img" aria-label="Black silhouette of a sea-goat, the Capricorn emblem">
        <circle cx="200" cy="204" r="94" fill="url(#emblem-fill)"/>
      </g>
    </svg>

    <p class="author">RM Calloway</p>

    <div class="corner-ornament corner-ornament--bottom-left" role="img" aria-label="Small corner flourish"></div>
    <div class="corner-ornament corner-ornament--bottom-right" role="img" aria-label="Small corner flourish"></div>
  </section>
</main>
</body>
</html>
```